Book Cover - Life Lessons Book

I have written a book for my sons who are graduating high school and college. Working title is "Chart Your Compass.....38 Lessons Learned at Home" I am looking for the book to appeal to young adults and parents who would want to give this book to them. It is a 125 page book that will be hardback and paperback - probably 5x8 or 6x9.
Updates

Reason: Altered some of the design elements based on the first submissions received. Would really like to have designs by Monday, May 15, 2016 but could not force a 2 day extension.

Target Market(s)

Young adults -- graduates, 20-3- year olds. And, parents would would give a book to their kids

Industry/Entity Type

Book Publisher

Font styles to use
Serif

Requirements
Must have
• Great design. It is a book cover so needs to catch the attention.
Nice to have
• I am open to more animated/playful/modern look or a more traditional look. Just would like to appeal to young adults and parents.
Should not have
• Anything in poor taste

```html
<!DOCTYPE html>
<html lang="en">
<head>
<meta charset="utf-8">
<title>Chart Your Compass – Book Cover</title>
<link href="https://fonts.googleapis.com/css2?family=Marcellus&family=Anton&family=Libre+Caslon+Text&display=swap" rel="stylesheet">
<style>
  :root {
    --ink: #151515;
    --navy: #1b2d6b;
    --paper-light: #f4f5f5;
    --paper-mid: #e2e4e5;
    --paper-dark: #d3d6d8;
  }
  html, body {
    margin: 0;
    padding: 0;
    width: 886px;
    height: 1200px;
    overflow: hidden;
    background: var(--paper-light);
  }
  .cover {
    position: relative;
    width: 886px;
    height: 1200px;
    overflow: hidden;
  }
  .cover__texture {
    position: absolute;
    inset: 0;
    width: 100%;
    height: 100%;
  }
  .title-line {
    position: absolute;
    left: 0;
    right: 0;
    margin: 0;
    line-height: 1;
    white-space: nowrap;
    text-align: center;
    font-weight: 400;
    font-family: "Marcellus", serif;
    color: var(--ink);
  }
  .title-main {
    top: 29px;
    font-size: 215px;
    letter-spacing: 2px;
    padding-left: 34px;
  }
  .title-your {
    top: 241px;
    font-size: 90px;
    padding-left: 88px;
  }
  .title-place {
    top: 313px;
    font-size: 136px;
    padding-left: 134px;
  }
  .lessons__number {
    position: absolute;
    left: 110px;
    top: 508px;
    font-family: "Anton", sans-serif;
    font-size: 345px;
    line-height: 0.8;
    letter-spacing: -5px;
    color: var(--navy);
  }
  .lessons__word {
    position: absolute;
    font-family: "Marcellus", serif;
    line-height: 1;
    color: var(--navy);
    white-space: nowrap;
  }
  .lessons__word--first {
    left: 470px;
    top: 504px;
    font-size: 115px;
  }
  .lessons__word--second {
    left: 476px;
    top: 667px;
    font-size: 82px;
  }
  .lessons__word--connector {
    left: 300px;
    top: 767px;
    font-size: 150px;
  }
  .lessons__word--last {
    left: 470px;
    top: 767px;
    font-size: 150px;
  }
  .author {
    position: absolute;
    left: 0;
    right: 0;
    top: 1106px;
    margin: 0;
    text-align: center;
    padding-left: 28px;
    font-family: "Libre Caslon Text", serif;
    font-size: 66px;
    line-height: 1;
    color: var(--ink);
    letter-spacing: -1px;
    transform: scaleX(0.86);
  }
</style>
</head>
<body>
  <main class="cover">
    <svg class="cover__texture" viewBox="0 0 886 1200" role="img" aria-label="Pale grey geometric triangle pattern background" preserveAspectRatio="none">
      <defs>
        <linearGradient id="paperTone" x1="0" y1="0" x2="1" y2="1">
          <stop offset="0" stop-color="#eef0f0"/>
          <stop offset="0.5" stop-color="#e1e3e4"/>
          <stop offset="1" stop-color="#eceeee"/>
        </linearGradient>
      </defs>
      <rect width="886" height="1200" fill="url(#paperTone)"/>
    </svg>

    <h1 class="title-line title-main">Chart</h1>
    <p class="title-line title-your">Your</p>
    <p class="title-line title-place">Compass...</p>

    <div class="lessons">
      <span class="lessons__number">38</span>
      <span class="lessons__word lessons__word--first">Lessons</span>
      <span class="lessons__word lessons__word--second">Learned</span>
      <span class="lessons__word lessons__word--connector">at</span>
      <span class="lessons__word lessons__word--last">Home</span>
    </div>

    <p class="author">Author Name</p>
  </main>
</body>
</html>
```